Kestrel Roofing & Restoration Business Card Design

Lookiing for a double sided business card design that will have rounded corners, will look good with Spot UV, Soft Laminate, or Gloss
Front of card should have Logo, Name and Contact Info, License numbers
Back of card should have Logo, maybe other small details

```html
<!DOCTYPE html>
<html lang="en">
<head>
<meta charset="utf-8">
<title>Kestrel Roofing &amp; Restoration – Business Card</title>
<link rel="stylesheet" href="https://fonts.googleapis.com/css2?family=Noto+Serif:wght@400;700&display=swap">
<style>
  :root {
    --backdrop: #e4e4e4;
    --card: #222222;
    --card-edge: #111111;
    --ink: #ffffff;
    --ink-soft: #e8e8e8;
    --icon: #f2e13a;
    --accent: #38c6ee;
  }
  * { margin: 0; padding: 0; box-sizing: border-box; }
  html, body {
    width: 1200px; height: 1200px; overflow: hidden;
    background: var(--backdrop);
    font-family: "Noto Serif", Georgia, serif;
  }
  .canvas {
    width: 1200px; height: 1200px;
    display: flex; flex-direction: column;
    align-items: center; justify-content: center; gap: 60px;
  }
  .card {
    position: relative;
    width: 700px; height: 400px;
    background: var(--card);
    border-radius: 28px;
    overflow: hidden;
    box-shadow: 0 6px 0 var(--card-edge), 0 18px 30px rgba(0,0,0,.18);
    color: var(--ink);
  }
  .holder-name {
    position: absolute; left: 46px; top: 44px;
    font-size: 30px; font-weight: 400; letter-spacing: .2px;
  }
  .holder-name strong { font-weight: 700; }
  .contact-list {
    position: absolute; left: 46px; top: 122px;
    list-style: none;
    font-size: 15px; line-height: 23px; color: var(--ink-soft);
  }
  .contact-list li { display: flex; align-items: center; gap: 12px; height: 23px; }
  .contact-icon { width: 16px; height: 16px; flex: none; }
  .contact-icon.blank { visibility: hidden; }
  .wordmark {
    position: absolute; display: flex; align-items: center; gap: 12px;
    font-weight: 700; color: var(--ink); line-height: 1.1;
  }
  .wordmark-square { background: var(--accent); flex: none; }
  .front .wordmark { right: 46px; top: 236px; font-size: 22px; }
  .front .wordmark-square { width: 16px; height: 16px; }
  .back .wordmark {
    left: 50%; top: 50%; transform: translate(-50%, -50%);
    font-size: 30px;
  }
  .back .wordmark-square { width: 22px; height: 22px; }
  .accent-tab {
    position: absolute; right: 0; bottom: 0;
    width: 230px; height: 40px;
    background: var(--accent);
    border-top-left-radius: 20px;
  }
</style>
</head>
<body>
<main class="canvas">
  <section class="card front" aria-label="Card front">
    <h1 class="holder-name">Marlo <strong>Vance</strong></h1>
    <ul class="contact-list">
      <li>
        <svg class="contact-icon" viewBox="0 0 16 16"><rect x="4" y="1.5" width="8" height="13" rx="1.5" fill="none" stroke="var(--icon)" stroke-width="1.4"/><circle cx="8" cy="12" r=".9" fill="var(--icon)"/></svg>
        503 555 0148
      </li>
      <li>
        <svg class="contact-icon" viewBox="0 0 16 16"><rect x="1.5" y="3.5" width="13" height="9" fill="none" stroke="var(--icon)" stroke-width="1.4"/><path d="M1.5 3.5 8 9l6.5-5.5" fill="none" stroke="var(--icon)" stroke-width="1.4"/></svg>
        Lic: #40718263
      </li>
      <li>
        <svg class="contact-icon" viewBox="0 0 16 16"><path d="M8 15s5-5.2 5-9A5 5 0 0 0 3 6c0 3.8 5 9 5 9z" fill="var(--icon)"/><circle cx="8" cy="6" r="1.8" fill="var(--card)"/></svg>
        www.kestrelroofing.com
      </li>
      <li><span class="contact-icon blank"></span>marlo@kestrelroofing.com</li>
      <li><span class="contact-icon blank"></span>Fairview, 100, Oregon.</li>
    </ul>
    <div class="wordmark">
      <span class="wordmark-square"></span>
      <span>Kestrel Roofing<br>&amp; Restoration</span>
    </div>
    <div class="accent-tab"></div>
  </section>

  <section class="card back" aria-label="Card back">
    <div class="wordmark">
      <span class="wordmark-square"></span>
      <span>Kestrel Roofing<br>&amp; Restoration</span>
    </div>
  </section>
</main>
</body>
</html>
```